Business Card Design

personal trainer and group fitness ....indoor and outdoor. want to deal with people all sexes/ages. Also am a swim teacher/ and will do aqua areobics.
would like to see a simple symbol......maybe a kettle bell / with a hand weight in front of it or combined with water/ outdoors background ????????? not sure . grey with hot pink or yellow colours.however not sure on that either.
Live at Lake Macquarie NSW so am based between water and mountains. Want to depict happy/ fun /healthy/ everyone.
Updates

Project Deadline Extended
Reason: Would like more action on some ideas ...will post a photo of an idea i like over weekend...hopefully someone will work off that

HI , I am still waiting to see some more designs... I have updated profile with a card that I like the idea of with notes of changes to it.   Would like to see some new designs asap.    Pretty please :) Dannie

Target Market(s)

all ages . mainly 20-55 .

Industry/Entity Type

Personal Trainer

Contact Information for Business Card

T Rell Fitness
Dannie Fairholt
Owner/Trainer

Group and Personal Training
0417 630925
Wattlebrook WA
trfit@quellmail.example
(please put facebook logo somewhere too) ALSO please put instagram logo on it
abn: 42 587 301 764
on the back "Life does not getter better by chance ......It gets better by change"

Colors
e34197
fbed23
cbcbcb
606060

Requirements
Nice to have
• like the idea of a funky bold font , not 100% onb colors below just something i like
PLease see card attached....i made this up... I want the kettle bell/handweight like this....but i dont want the fist in the middle. PLEASE note I only want TRell fitness now not fitness and wellbeing.

```html
<!DOCTYPE html>
<html lang="en">
<head>
<meta charset="utf-8">
<title>T Rell Fitness — Business Card</title>
<link rel="stylesheet" href="https://fonts.googleapis.com/css2?family=Play:wght@400;700&family=Kaushan+Script&display=swap">
<style>
  :root {
    --backdrop: #d9d9db;
    --card-front: #1c1b1d;
    --card-back: #2a2b2d;
    --hot-pink: #e3199a;
    --white: #f4f4f4;
    --divider: #8a8a8c;
    --photo-dark: #141415;
    --photo-mid: #3a3b3d;
  }
  * { box-sizing: border-box; margin: 0; padding: 0; }
  html, body {
    width: 1200px; height: 900px; overflow: hidden;
    background: var(--backdrop);
  }
  .canvas {
    width: 1200px; height: 900px;
    display: flex; flex-direction: column; align-items: center; justify-content: center;
    gap: 40px;
  }
  .card {
    width: 640px; height: 390px;
    position: relative;
    box-shadow: 0 8px 24px rgba(0,0,0,0.25);
    font-family: "Play", sans-serif;
    color: var(--white);
    overflow: hidden;
  }

  /* Tagline side */
  .card--tagline { background: var(--card-front); }
  .card--tagline .brand-name {
    position: absolute; left: 0; right: 0; top: 118px;
    text-align: center;
    font-size: 52px; font-weight: 700; letter-spacing: 2px;
    color: var(--hot-pink);
  }
  .tagline {
    position: absolute; left: 60px; top: 218px;
    font-family: "Kaushan Script", cursive;
    font-size: 32px; color: var(--white);
    white-space: nowrap;
  }
  .tagline-answer {
    position: absolute; right: 48px; top: 268px;
    font-size: 17px; color: var(--hot-pink);
    white-space: nowrap;
  }

  /* Details side */
  .card--details { background: var(--card-back); }
  .brand-block {
    position: absolute; left: 36px; top: 118px; width: 300px;
    text-align: center;
  }
  .card--details .brand-name {
    font-size: 38px; font-weight: 700; letter-spacing: 1px;
    color: var(--hot-pink);
    white-space: nowrap;
  }
  .service-line {
    margin-top: 10px;
    font-size: 17px; color: var(--white);
  }
  .equipment-photo {
    position: absolute; left: 40px; bottom: 0; width: 300px; height: 150px;
    background: radial-gradient(ellipse at 50% 70%, var(--photo-mid) 0%, var(--photo-dark) 55%, var(--card-back) 80%);
    opacity: 0.9;
  }
  .divider {
    position: absolute; left: 352px; top: 30px; width: 1px; height: 240px;
    background: var(--divider);
  }
  .contact {
    position: absolute; left: 378px; top: 42px;
    font-size: 17px; line-height: 1.3;
    white-space: nowrap;
  }
  .contact-name {
    font-size: 23px; font-weight: 700; color: var(--hot-pink);
  }
  .contact-role { margin-bottom: 16px; }
  .contact-label { color: var(--hot-pink); }
  .contact-location { margin-top: 24px; }
  .social {
    position: absolute; left: 430px; top: 298px;
    display: flex; gap: 14px;
  }
  .social-mark {
    width: 20px; height: 20px; border-radius: 4px;
    background: var(--hot-pink);
  }
</style>
</head>
<body>
  <main class="canvas">
    <section class="card card--tagline">
      <div class="brand-name">T Rell Fitness</div>
      <div class="tagline">Life doesnt get better by chance</div>
      <div class="tagline-answer">......It gets better by change</div>
    </section>

    <section class="card card--details">
      <div class="equipment-photo" role="img" aria-label="Photo of three black kettlebells of different sizes"></div>
      <div class="brand-block">
        <div class="brand-name">T Rell Fitness</div>
        <div class="service-line">Group and Personal Training</div>
      </div>
      <div class="divider"></div>
      <div class="contact">
        <div class="contact-name">Dannie Fairholt</div>
        <div class="contact-role">Owner/Trainer</div>
        <div><span class="contact-label">P:</span> 0417 630925</div>
        <div><span class="contact-label">E:</span> trfit@quellmail.example</div>
        <div><span class="contact-label">Abn:</span> 42 587 301 764</div>
        <div class="contact-location">Wattlebrook WA</div>
      </div>
      <div class="social" aria-label="Social media">
        <span class="social-mark"></span>
        <span class="social-mark"></span>
      </div>
    </section>
  </main>
</body>
</html>
```